Kestrelmoor Advisory Services LLC
The Quiet Hand Consutants
Project: Kestrelmoor Advisory Services LLC
Kestrelmoor Advisory Services LLC - Financial Services
Creative Brief
Professional
Warrick Dunstan Hollowell
Senior Managing Director
388 West 19th Street New York, N.T. 10024
whollowell@kmaservices.net
KESTRELMOORADVISORYSERVICES.COM

```html
<!DOCTYPE html>
<html lang="en">
<head>
<meta charset="utf-8">
<title>Kestrelmoor Advisory Services – Business Card</title>
<link href="https://fonts.googleapis.com/css2?family=Caladea:wght@400;700&display=swap" rel="stylesheet">
<style>
  :root {
    --backdrop: #e6e6e6;
    --card: #ffffff;
    --navy: #1d3f7a;
    --blue: #1f6fc0;
    --blue-light: #4ea3e6;
    --gold: #b88a2e;
    --ink: #3a3a3a;
    --rule: #c9c9c9;
  }
  * { margin: 0; padding: 0; box-sizing: border-box; }
  html, body {
    width: 1200px; height: 780px; overflow: hidden;
    background: var(--backdrop);
    font-family: "Caladea", Georgia, serif;
  }
  .business-card {
    position: absolute; left: 40px; top: 70px;
    width: 1120px; height: 640px;
    background: var(--card);
    border-radius: 28px;
    overflow: hidden;
    box-shadow: 0 6px 24px rgba(0,0,0,.15);
  }
  .wave-band { position: absolute; left: 0; top: 0; width: 1120px; height: 640px; }
  .brand {
    position: absolute; left: 60px; top: 170px; width: 420px;
    text-align: center; color: var(--navy);
  }
  .brand-dot {
    width: 110px; height: 110px; border-radius: 50%;
    background: var(--blue); margin: 0 auto 26px;
  }
  .brand-name {
    font-size: 40px; font-weight: 400; line-height: 1.05;
    letter-spacing: 1px;
  }
  .divider {
    position: absolute; left: 520px; top: 120px;
    width: 2px; height: 360px; background: var(--rule);
  }
  .details { position: absolute; left: 550px; top: 110px; }
  .person-name { font-size: 34px; font-weight: 700; color: var(--navy); }
  .person-title { font-size: 25px; font-weight: 700; color: var(--gold); margin-top: 2px; }
  .address { font-size: 23px; color: var(--ink); margin-top: 32px; line-height: 1.25; }
  .contact-list { list-style: none; margin-top: 26px; }
  .contact-list li {
    display: flex; align-items: center; gap: 14px;
    font-size: 22px; color: var(--ink); height: 34px;
  }
  .contact-icon { width: 20px; height: 20px; fill: var(--navy); flex: none; }
</style>
</head>
<body>
<main class="business-card">
  <svg class="wave-band" viewBox="0 0 1120 640" aria-hidden="true">
    <defs>
      <linearGradient id="bandFill" x1="0" y1="0" x2="1" y2="0">
        <stop offset="0" stop-color="var(--blue)"/>
        <stop offset="0.55" stop-color="var(--blue-light)"/>
        <stop offset="1" stop-color="var(--blue)"/>
      </linearGradient>
    </defs>
    <path d="M0 585 C 320 500, 640 640, 1120 500 L1120 640 L0 640 Z" fill="url(#bandFill)"/>
    <path d="M0 560 C 320 470, 640 610, 1120 470" fill="none" stroke="var(--gold)" stroke-width="9"/>
    <path d="M0 540 C 340 460, 660 590, 1120 452" fill="none" stroke="var(--rule)" stroke-width="2"/>
  </svg>

  <div class="brand">
    <div class="brand-dot"></div>
    <div class="brand-name">Kestrelmoor<br>Advisory Services</div>
  </div>

  <div class="divider"></div>

  <section class="details">
    <h1 class="person-name">Warrick Dunstan Hollowell</h1>
    <p class="person-title">Senior Managing Director</p>
    <p class="address">388 West 19th Street<br>New York, N.T. 10024</p>
    <ul class="contact-list">
      <li><svg class="contact-icon" viewBox="0 0 20 20"><path d="M4 2l4 3-2 3c1 2 3 4 5 5l3-2 3 4-3 3C8 18 2 12 1 5z"/></svg>646-555-0142</li>
      <li><svg class="contact-icon" viewBox="0 0 20 20"><rect x="5" y="1" width="10" height="18" rx="2"/><rect x="7" y="3" width="6" height="10" fill="#fff"/></svg>201-555-0187</li>
      <li><svg class="contact-icon" viewBox="0 0 20 20"><rect x="2" y="8" width="16" height="10" rx="1"/><rect x="5" y="2" width="10" height="7" fill="none" stroke="currentColor" stroke-width="2" style="stroke:var(--navy)"/></svg>917-555-0123</li>
      <li><svg class="contact-icon" viewBox="0 0 20 20"><text x="10" y="16" text-anchor="middle" font-size="18" font-weight="700" font-family="Arial, sans-serif">@</text></svg>whollowell@kmaservices.net</li>
      <li><svg class="contact-icon" viewBox="0 0 20 20"><circle cx="10" cy="10" r="8" fill="none" stroke-width="2" style="stroke:var(--navy)"/><ellipse cx="10" cy="10" rx="3.5" ry="8" fill="none" stroke-width="1.5" style="stroke:var(--navy)"/><line x1="2" y1="10" x2="18" y2="10" stroke-width="1.5" style="stroke:var(--navy)"/></svg>kestrelmooradvisoryservices.com</li>
    </ul>
  </section>
</main>
</body>
</html>
```